I need business cards for a new company called BrightHarbor Healthcare Education Consulting. We provide a comprehensive suite of consulting and education services designed to support healthcare organizations, educational institutions, pre-professionals, and professionals in achieving excellence. Our services are tailored to address the dynamic needs of the healthcare sector, from operational efficiency to workforce development and beyond. We provide customized solutions for individuals and organizations seeking to enhance knowledge, compliance, and care delivery through innovative and effective educational programs. We would like to see designs that use the colors blue and green. Tagline: "Where Learning Meets Healthcare Innovation". QR code linking to website and LinkedIn profile. If possible, reflect the consulting and education aspect of the business with symbols or phrases that emphasize guidance, learning, or expertise. Logo is attached.

```html
<!DOCTYPE html>
<html lang="en">
<head>
<meta charset="utf-8">
<title>BrightHarbor Business Card</title>
<link href="https://fonts.googleapis.com/css2?family=Montserrat:wght@400;500;600;800&display=swap" rel="stylesheet">
<style>
  :root {
    --page-bg: #e6e8e8;
    --mint: #72c7a8;
    --mint-light: #8fd4ba;
    --mint-deep: #3fa883;
    --harbor-blue: #2f7fb8;
    --harbor-blue-soft: #e3eff8;
    --ink: #1e2626;
    --ink-soft: #4b5757;
    --card-white: #ffffff;
  }
  * { box-sizing: border-box; margin: 0; padding: 0; }
  html, body {
    width: 974px;
    height: 1200px;
    overflow: hidden;
    background: var(--page-bg);
    font-family: "Montserrat", sans-serif;
    color: var(--ink);
  }
  .canvas {
    width: 974px;
    height: 1200px;
    display: flex;
    flex-direction: column;
    align-items: center;
    justify-content: center;
    gap: 80px;
  }
  .card {
    width: 760px;
    height: 434px;
    border-radius: 6px;
    position: relative;
    overflow: hidden;
    box-shadow: 0 2px 6px rgba(0,0,0,0.12);
  }

  /* Front: mint card with tonal wordmark */
  .card-front {
    background: var(--mint);
    display: flex;
    align-items: center;
    justify-content: center;
  }
  .front-mark {
    display: flex;
    align-items: center;
    gap: 22px;
  }
  .front-mark__square {
    width: 64px;
    height: 64px;
    background: var(--mint-light);
  }
  .front-mark__name {
    font-weight: 800;
    font-size: 68px;
    letter-spacing: -1px;
    color: var(--mint-light);
  }
  .front-band {
    position: absolute;
    left: 0;
    right: 0;
    bottom: 0;
    height: 18px;
    background: var(--harbor-blue);
  }

  /* Back: white card with details */
  .card-back {
    background: var(--card-white);
    padding: 54px 60px 0 60px;
  }
  .brand {
    display: flex;
    align-items: center;
    gap: 16px;
  }
  .brand__square {
    width: 44px;
    height: 44px;
    background: var(--mint-deep);
  }
  .brand__name {
    font-weight: 800;
    font-size: 44px;
    letter-spacing: -0.5px;
    color: var(--ink);
  }
  .brand__sub {
    margin-top: 8px;
    margin-left: 60px;
    font-size: 12px;
    font-weight: 600;
    letter-spacing: 2.4px;
    color: var(--harbor-blue);
  }
  .person {
    margin-top: 34px;
  }
  .person__name {
    font-size: 22px;
    font-weight: 600;
  }
  .person__title {
    margin-top: 4px;
    font-size: 13px;
    color: var(--ink-soft);
  }
  .contacts {
    list-style: none;
    margin-top: 20px;
    display: grid;
    grid-template-columns: 210px 290px;
    row-gap: 12px;
    column-gap: 20px;
    width: 520px;
  }
  .contact {
    display: flex;
    align-items: center;
    gap: 10px;
    font-size: 13px;
    color: var(--ink-soft);
    white-space: nowrap;
  }
  .contact__icon {
    width: 22px;
    height: 22px;
    border-radius: 50%;
    background: var(--harbor-blue);
    display: flex;
    align-items: center;
    justify-content: center;
    flex-shrink: 0;
  }
  .qr-area {
    position: absolute;
    right: 60px;
    bottom: 54px;
    width: 116px;
    height: 116px;
    background: var(--harbor-blue-soft);
    border: 6px solid var(--harbor-blue);
    border-radius: 4px;
  }
  .qr-caption {
    position: absolute;
    right: 60px;
    bottom: 178px;
    width: 116px;
    text-align: center;
    font-size: 10px;
    font-weight: 600;
    letter-spacing: 1px;
    color: var(--harbor-blue);
  }
  .tagline {
    position: absolute;
    left: 60px;
    bottom: 42px;
    font-size: 12px;
    font-weight: 500;
    letter-spacing: 1px;
    color: var(--mint-deep);
  }
  .back-band {
    position: absolute;
    left: 0;
    right: 0;
    bottom: 0;
    height: 18px;
    background: linear-gradient(90deg, var(--mint) 0%, var(--mint) 55%, var(--harbor-blue) 100%);
  }
</style>
</head>
<body>
<main class="canvas">

  <section class="card card-front" aria-label="Card front">
    <div class="front-mark">
      <span class="front-mark__square"></span>
      <span class="front-mark__name">BrightHarbor</span>
    </div>
    <div class="front-band"></div>
  </section>

  <section class="card card-back" aria-label="Card back">
    <div class="brand">
      <span class="brand__square"></span>
      <span class="brand__name">BrightHarbor</span>
    </div>
    <p class="brand__sub">HEALTHCARE EDUCATION CONSULTING</p>

    <div class="person">
      <p class="person__name">Dana Whitfield</p>
      <p class="person__title">Founder &amp; Lead Consultant</p>
    </div>

    <ul class="contacts">
      <li class="contact">
        <span class="contact__icon">
          <svg width="12" height="12" viewBox="0 0 24 24" fill="#fff"><path d="M6.6 10.8a15.1 15.1 0 0 0 6.6 6.6l2.2-2.2a1 1 0 0 1 1-.25 11.4 11.4 0 0 0 3.6.57 1 1 0 0 1 1 1V20a1 1 0 0 1-1 1A17 17 0 0 1 3 4a1 1 0 0 1 1-1h3.5a1 1 0 0 1 1 1c0 1.25.2 2.45.57 3.57a1 1 0 0 1-.25 1z"/></svg>
        </span>
        +1 (555) 214-7730
      </li>
      <li class="contact">
        <span class="contact__icon">
          <svg width="12" height="12" viewBox="0 0 24 24" fill="none" stroke="#fff" stroke-width="2.4"><rect x="3" y="5" width="18" height="14" rx="1"/><path d="M3 6l9 7 9-7"/></svg>
        </span>
        dana@brightharbor.example
      </li>
      <li class="contact">
        <span class="contact__icon">
          <svg width="12" height="12" viewBox="0 0 24 24" fill="none" stroke="#fff" stroke-width="2.2"><circle cx="12" cy="12" r="9"/><path d="M3 12h18M12 3c3 3 3 15 0 18M12 3c-3 3-3 15 0 18"/></svg>
        </span>
        www.brightharbor.example
      </li>
      <li class="contact">
        <span class="contact__icon">
          <svg width="12" height="12" viewBox="0 0 24 24" fill="#fff"><path d="M12 2a7 7 0 0 0-7 7c0 5 7 13 7 13s7-8 7-13a7 7 0 0 0-7-7zm0 9.5A2.5 2.5 0 1 1 12 6.5a2.5 2.5 0 0 1 0 5z"/></svg>
        </span>
        48 Harbor Lane, Suite 2, Springfield
      </li>
    </ul>

    <p class="qr-caption">SCAN TO CONNECT</p>
    <div class="qr-area" role="img" aria-label="QR code linking to the website and LinkedIn profile"></div>

    <p class="tagline">Where Learning Meets Healthcare Innovation</p>
    <div class="back-band"></div>
  </section>

</main>
</body>
</html>
```